Professional Website for Brightfold Laundry Company

Brightfold Laundry Company is a family-owned laundry service provider that has been serving Midtown Atlanta for over 45 years. We provide express clothing and linen washing services to residential and commercial clients in Atlanta and surrounding areas.

The final website and logo design should convey professionalism and give the customer a sense of security in having their personal items laundered with us.

Target Market(s)

Commercial Businesses and high net worth personal customers

Industry/Entity Type

Professional Laundry Services

Coding

Coded - Design and coding required

Number of Pages Required

5+ page

Font styles to use
Sans Serif

Colors
0054AA
0677BA
7BADD7
CADEEF
E8F1F8

Requirements
Must have
• I would like to have the following elements on my website: 1. Blog page 2. Contact Us Form 3. Sign up for service (sample attached) 4. Sections outlined in the content copy page 5. Links to social media accounts.
Nice to have
• A great example is https://www.quillmarsh.example/laundry-pick-up-and-delivery/?utm_term=pick%20up%20and%20delivery%20laundry%20service&utm_campaign=*QM%20United%20States%20%7C%20Search%20(Broad%20KWs)&utm_source=zorvik&utm_medium=ppc&hsa_acc=1111111111&hsa_cam=22222222222&hsa_grp=3333333333333333&hsa_ad=&hsa_src=o&hsa_tgt=kwd-44444444444444:loc-100&hsa_kw=pick%20up%20and%20delivery%20laundry%20service&hsa_mt=e&hsa_net=zorvik&hsa_ver=3&msclkid=00000000000000000000000000000000

```html
<!DOCTYPE html>
<html lang="en">
<head>
<meta charset="utf-8">
<title>Brightfold Laundry Company</title>
<link rel="stylesheet" href="https://fonts.googleapis.com/css2?family=Josefin+Sans:wght@300;400;600;700&family=Nunito+Sans:wght@400;600;700&display=swap">
<style>
:root{
  --ink:#111111;
  --text:#333333;
  --muted:#666666;
  --blob:#ececec;
  --line:#bdbdbd;
  --white:#ffffff;
  --brand-deep:#0054AA;
  --brand-mid:#0677BA;
  --brand-soft:#7BADD7;
  --brand-pale:#CADEEF;
  --brand-mist:#E8F1F8;
  --head:"Josefin Sans",sans-serif;
  --body:"Nunito Sans",sans-serif;
}
*{box-sizing:border-box;margin:0;padding:0}
html,body{width:1200px;height:3916px;overflow:hidden;background:var(--white)}
body{position:relative;font-family:var(--body);color:var(--text)}
.abs{position:absolute}
a{color:inherit;text-decoration:none}
.btn{position:absolute;display:flex;align-items:center;justify-content:center;gap:6px;background:var(--ink);color:var(--white);font-family:var(--head);font-weight:600;font-size:13px;letter-spacing:1.2px;text-transform:uppercase;white-space:nowrap}
.eyebrow{position:absolute;font-family:var(--head);font-weight:400;letter-spacing:3px;text-transform:uppercase;color:var(--ink);white-space:nowrap}
.heading{position:absolute;font-family:var(--head);font-weight:700;text-transform:uppercase;color:var(--ink);line-height:1.1;white-space:nowrap}
.copy{position:absolute;font-size:13.5px;line-height:23px;color:var(--text)}
.photo{position:absolute}

/* brand name (header and footer) */
.brand{position:absolute;left:172px;display:flex;align-items:center;gap:9px;font-family:var(--head);font-weight:600;font-size:14px;line-height:17px;letter-spacing:3px;color:var(--ink)}
.brand-dot{width:8px;height:8px;border-radius:50%;background:var(--ink);flex:none}
.brand-name{display:block;text-align:center}

/* header */
.main-nav{position:absolute;left:328px;top:39px;width:566px;display:flex;justify-content:space-between;font-family:var(--head);font-size:12px;letter-spacing:1.2px;color:var(--ink);white-space:nowrap}

/* hero */
.hero{position:absolute;left:0;top:85px;width:1200px;height:466px;background:linear-gradient(90deg,#fafafa 0%,#f1f1f0 45%,#e9e7e2 70%,#f3f2ee 100%)}
.hero-figure{position:absolute;left:730px;top:0;width:250px;height:466px;background:linear-gradient(180deg,#e8d8cc 0%,#e9e2c9 45%,#2f9a55 70%,#1f8a45 100%);border-radius:110px 110px 0 0}
.slider-dots{position:absolute;top:483px;left:174px;display:flex;gap:18px}
.slider-dots span{width:40px;height:2px;background:#d2d2d2}
.slider-dots span.active{background:var(--ink)}

/* services */
.service-grid{position:absolute;left:600px;top:1270px;width:440px;display:grid;grid-template-columns:repeat(3,1fr);row-gap:28px}
.service{display:flex;flex-direction:column;align-items:center;text-align:center;font-family:var(--head);font-size:14px;line-height:22px;color:var(--ink)}
.service-icon{width:52px;height:52px;border-radius:10px;margin-bottom:10px}

/* blog */
.blog-card{position:absolute;top:2475px;width:268px;height:348px;background:var(--white);box-shadow:0 4px 14px rgba(0,0,0,.07)}
.blog-image{width:268px;height:176px}
.date-badge{position:absolute;left:12px;top:12px;width:37px;height:50px;background:var(--ink);color:var(--white);text-align:center;font-family:var(--head)}
.date-badge small{display:block;font-size:10px;letter-spacing:1px;padding-top:6px}
.date-badge b{display:block;font-size:22px;line-height:24px}
.blog-title{position:absolute;left:9px;top:196px;font-family:var(--head);font-weight:600;font-size:14px;color:var(--ink);white-space:nowrap}
.blog-text{position:absolute;left:9px;top:218px;width:250px;font-size:13px;line-height:20px;color:var(--text)}
.blog-more{position:absolute;left:9px;top:294px;font-family:var(--head);font-weight:600;font-size:12.5px;letter-spacing:1.2px;color:var(--ink);border-bottom:1px solid var(--ink);padding-bottom:2px}
.slider-arrow{position:absolute;top:2548px;width:44px;height:44px;border-radius:50%;background:#777;display:flex;align-items:center;justify-content:center}

/* contact */
.contact-card{position:absolute;left:174px;top:2954px;width:853px;height:407px;background:var(--white);box-shadow:0 4px 16px rgba(0,0,0,.06)}
.field{position:absolute;left:437px;width:375px;border-bottom:1px solid var(--line);font-size:13px;color:var(--text);padding-bottom:9px}

/* newsletter */
.newsletter-title{position:absolute;left:240px;top:3501px;width:262px;text-align:right;font-family:var(--head);font-weight:600;font-size:17px;letter-spacing:1.5px;color:var(--ink);white-space:nowrap}

/* footer */
.foot-title{position:absolute;font-family:var(--head);font-weight:600;font-size:14px;letter-spacing:2px;color:var(--ink);white-space:nowrap}
.foot-list{position:absolute;list-style:none;font-size:12.5px;color:var(--text);white-space:nowrap}
.foot-list li{height:32.5px}
.divider{position:absolute;top:3635px;width:1px;height:168px;background:#cfcfcf}
.divider::after{content:"";position:absolute;left:-1px;top:58px;width:3px;height:22px;background:var(--ink)}
.social{position:absolute;top:3675px;width:30px;height:30px;border:1px solid var(--ink)}
.contact-line{position:absolute;left:815px;font-size:12px;color:var(--text);display:flex;gap:7px;line-height:25px;white-space:nowrap}
</style>
</head>
<body>

<!-- header -->
<header>
  <a class="brand" href="#" style="top:29px"><span class="brand-dot"></span><span class="brand-name">BRIGHTFOLD<br>LAUNDRY</span></a>
  <nav class="main-nav">
    <a href="#">HOME</a><a href="#">ABOUT US</a><a href="#">WHY CHOOSE US</a><a href="#">SERVICES</a><a href="#">BLOG</a><a href="#">CONTACT US</a>
  </nav>
  <a class="btn" href="#" style="left:911px;top:26px;width:116px;height:39px">SIGN UP ›</a>
</header>

<!-- hero -->
<section>
  <div class="hero" role="img" aria-label="Bright bedroom with a smiling laundry attendant in a green apron holding folded linens">
    <div class="hero-figure"></div>
  </div>
  <p class="eyebrow" style="left:174px;top:166px;font-size:22px;letter-spacing:3.5px">ATLANTA FOR OVER</p>
  <h1 class="heading" style="left:172px;top:200px;font-size:78px;line-height:1">45 YEARS</h1>
  <p class="copy" style="left:174px;top:283px;width:400px;font-size:16px;line-height:23px;color:var(--ink)">We are proud to offer high quality and convenient services to the area residents and business</p>
  <a class="btn" href="#" style="left:174px;top:353px;width:192px;height:38px">SIGN UP FOR SERVICE ›</a>
  <div class="slider-dots"><span class="active"></span><span></span><span></span></div>
</section>

<!-- about -->
<section>
  <div class="photo" role="img" aria-label="Woman loading white laundry from a basket beside washing machines" style="left:176px;top:616px;width:364px;height:424px;border-radius:22px;background:linear-gradient(135deg,#f2f0ed 0%,#d9d6d1 50%,#c6cfd8 100%)"></div>
  <div class="abs" style="left:551px;top:669px;height:360px;border-left:2px dotted #9a9a9a"></div>
  <p class="eyebrow" style="left:584px;top:660px;font-size:18px">ABOUT</p>
  <h2 class="heading" style="left:584px;top:686px;font-size:36px">BRIGHTFOLD LAUNDRY<br>COMPANY</h2>
  <p class="copy" style="left:584px;top:783px;width:448px">Brightfold Laundry Company is a family-owned laundry service provider that has been serving Midtown Atlanta for over 45 years. We are proud to offer high quality and convenient services to the area residents and business owners and strive to keep our customers' clothing in tip top shape.</p>
  <a class="btn" href="#" style="left:584px;top:920px;width:124px;height:40px">READ MORE ›</a>
</section>

<!-- decorative blobs -->
<svg class="abs" style="left:0;top:0" width="1200" height="3916" viewBox="0 0 1200 3916" aria-hidden="true">
  <path fill="#ececec" d="M0,1125 C160,1118 340,1110 480,1190 C630,1275 610,1420 570,1525 C530,1630 470,1700 300,1728 C190,1742 90,1705 0,1692 Z"/>
  <path fill="#ececec" d="M1200,1734 L930,1738 C720,1748 565,1860 545,2000 C525,2150 680,2238 880,2258 C960,2275 955,2390 1080,2392 C1150,2392 1200,2345 1200,2320 Z"/>
  <path fill="#ececec" d="M0,2867 C160,2848 340,2880 470,2954 L470,3361 C310,3380 230,3425 60,3455 L0,3462 Z"/>
  <g fill="none" stroke="#222" stroke-width="1.5">
    <circle cx="251" cy="1202" r="5"/>
    <circle cx="827" cy="1822" r="5"/>
    <circle cx="266" cy="2908" r="5"/>
  </g>
  <g fill="none" stroke="#555" stroke-width="1">
    <path d="M420,1231 L423,1240 L432,1243 L423,1246 L420,1255 L417,1246 L408,1243 L417,1240 Z"/>
    <path d="M998,1851 L1001,1860 L1010,1863 L1001,1866 L998,1875 L995,1866 L986,1863 L995,1860 Z"/>
    <path d="M193,3386 L196,3395 L205,3398 L196,3401 L193,3410 L190,3401 L181,3398 L190,3395 Z"/>
  </g>
  <g fill="#111">
    <path d="M357,1516 L359,1521 L364,1523 L359,1525 L357,1530 L355,1525 L350,1523 L355,1521 Z"/>
    <path d="M403,2926 L405,2931 L410,2933 L405,2935 L403,2940 L401,2935 L396,2933 L401,2931 Z"/>
  </g>
</svg>

<!-- services -->
<section>
  <h2 class="abs" style="left:174px;top:1280px;font-family:var(--head);font-size:39px;color:var(--ink);letter-spacing:.5px;white-space:nowrap"><span style="font-weight:300">OUR </span><span style="font-weight:700">SERVICES</span></h2>
  <p class="copy" style="left:174px;top:1344px;width:408px">Running a small business is not easy and the last thing you need is another tedious action item like doing laundry on your to-do list. Whether it is towels, linens or uniforms, outsourcing your launder needs to Brightfold Laundry Company will allow you to focus on your business.</p>
  <a class="btn" href="#" style="left:174px;top:1491px;width:124px;height:38px">READ MORE ›</a>
  <div class="photo" role="img" aria-label="Stack of folded shirts beside a blue and white steam iron" style="left:160px;top:1545px;width:456px;height:155px;background:linear-gradient(90deg,#c8d6e6 0%,#a9bfd8 45%,#e6eef6 62%,#4f8fd6 78%,#f2f4f7 100%);border-radius:20px 90px 10px 10px"></div>
  <div class="service-grid">
    <div class="service"><div class="service-icon" role="img" aria-label="Washing machine icon" style="background:var(--brand-pale)"></div>Commercial<br>Services</div>
    <div class="service"><div class="service-icon" role="img" aria-label="Iron icon" style="background:#f3e27a"></div>Light Commercial<br>Services</div>
    <div class="service"><div class="service-icon" role="img" aria-label="Laundry basket icon" style="background:#f4b66b"></div>Professional Laundry<br>Services</div>
    <div class="service"><div class="service-icon" role="img" aria-label="Delivery scooter icon" style="background:var(--brand-soft)"></div>Pickup and<br>Delivery</div>
    <div class="service"><div class="service-icon" role="img" aria-label="Folded clothes and iron icon" style="background:var(--brand-mid)"></div>Wash Dry<br>Fold</div>
    <div class="service"><div class="service-icon" role="img" aria-label="Shirt on hanger icon" style="background:#ef7b7b"></div>Dry<br>Cleaning</div>
  </div>
</section>

<!-- why choose -->
<section>
  <div class="photo" role="img" aria-label="Wicker basket of folded towels with white daisies" style="left:99px;top:1871px;width:464px;height:281px;border-radius:40px;background:linear-gradient(180deg,#bcd6ea 0%,#d8e9d2 35%,#cfa86a 60%,#f3f1ec 100%)"></div>
  <p class="eyebrow" style="left:614px;top:1879px;font-size:18px">WHY CHOOSE</p>
  <h2 class="heading" style="left:614px;top:1905px;font-size:36px">BRIGHTFOLD LAUNDRY<br>COMPANY</h2>
  <p class="abs" style="left:614px;top:2003px;font-size:16px;color:var(--ink)">We Help You Optimize Your Time</p>
  <p class="copy" style="left:614px;top:2033px;width:372px">Laundry is time consuming, especially for multi-tasking entrepreneurs. Brightfold Laundry Company makes a simple promise, we will give you your time back to focus on your business</p>
  <a class="btn" href="#" style="left:614px;top:2152px;width:124px;height:38px">READ MORE ›</a>
</section>

<!-- blog -->
<section>
  <p class="eyebrow" style="left:0;width:1200px;text-align:center;top:2386px;font-size:18px">BLOG</p>
  <h2 class="heading" style="left:0;width:1200px;text-align:center;top:2410px;font-size:37px">LATEST BLOG</h2>

  <article class="blog-card" style="left:174px">
    <div class="blog-image" role="img" aria-label="Blue basket full of colourful laundry" style="background:linear-gradient(135deg,#e7e2dc 0%,#d9a9a0 45%,#3f8fd0 80%)"></div>
    <div class="date-badge"><small>JUN</small><b>18</b></div>
    <h3 class="blog-title">Proin commodo lacus ut venenatis</h3>
    <p class="blog-text">Lorem ipsum dolor sit amet, coectetur adipiscing elit. Nam sit amet justo ac lorem tempus pretium sed eget nisi.</p>
    <a class="blog-more" href="#">READ MORE ›</a>
  </article>
  <article class="blog-card" style="left:466px">
    <div class="blog-image" role="img" aria-label="Mother and daughter doing laundry together" style="background:linear-gradient(135deg,#efe6da 0%,#d8c3ad 50%,#b9c3cb 100%)"></div>
    <div class="date-badge"><small>JUN</small><b>20</b></div>
    <h3 class="blog-title">Proin commodo lacus ut venenatis</h3>
    <p class="blog-text">Lorem ipsum dolor sit amet, coectetur adipiscing elit. Nam sit amet justo ac lorem tempus pretium sed eget nisi.</p>
    <a class="blog-more" href="#">READ MORE ›</a>
  </article>
  <article class="blog-card" style="left:758px">
    <div class="blog-image" role="img" aria-label="Man in a white shirt beside a washing machine" style="background:linear-gradient(135deg,#d9d5d0 0%,#f1efec 50%,#c9cdd2 100%)"></div>
    <div class="date-badge"><small>JUN</small><b>26</b></div>
    <h3 class="blog-title">Proin commodo lacus ut venenatis</h3>
    <p class="blog-text">Lorem ipsum dolor sit amet, coectetur adipiscing elit. Nam sit amet justo ac lorem tempus pretium sed eget nisi.</p>
    <a class="blog-more" href="#">READ MORE ›</a>
  </article>

  <a class="slider-arrow" href="#" aria-label="Previous" style="left:153px"><svg width="12" height="18" viewBox="0 0 12 18"><path d="M9,2 L3,9 L9,16" fill="none" stroke="#fff" stroke-width="1.6"/></svg></a>
  <a class="slider-arrow" href="#" aria-label="Next" style="left:1006px"><svg width="12" height="18" viewBox="0 0 12 18"><path d="M3,2 L9,9 L3,16" fill="none" stroke="#fff" stroke-width="1.6"/></svg></a>
</section>

<!-- contact -->
<section>
  <div class="contact-card">
    <div class="photo" role="img" aria-label="Mother hugging her young daughter beside a washing machine" style="left:0;top:0;width:406px;height:407px;background:linear-gradient(135deg,#b9c7d0 0%,#e6dcd2 40%,#c85c5a 70%,#d3dbe0 100%)"></div>
    <p class="eyebrow" style="left:437px;top:31px;font-size:18px">CONTACT US</p>
    <h2 class="heading" style="left:437px;top:56px;font-size:37px">GET IN TOUCH</h2>
    <div class="field" style="top:120px">Full Name</div>
    <div class="field" style="top:166px">Email Address</div>
    <div class="field" style="top:213px">Phone</div>
    <div class="field" style="top:260px;height:68px">Message</div>
    <a class="btn" href="#" style="left:440px;top:343px;width:124px;height:37px;gap:26px">SUBMIT <span>›</span></a>
  </div>
</section>

<!-- newsletter -->
<section>
  <h2 class="newsletter-title">NEWSLETTER SIGNUP</h2>
  <div class="abs" style="left:516px;top:3494px;width:401px;border-bottom:1px solid #888;padding-bottom:10px;font-size:13px;color:var(--muted)">Enter Email Address</div>
  <svg class="abs" style="left:899px;top:3495px" width="16" height="16" viewBox="0 0 16 16" aria-label="Send"><path d="M1,7 L15,1 L10,15 L8,9 Z" fill="#111"/></svg>
</section>

<!-- footer -->
<footer>
  <a class="brand" href="#" style="top:3620px"><span class="brand-dot"></span><span class="brand-name">BRIGHTFOLD<br>LAUNDRY</span></a>
  <a class="social" href="#" aria-label="Social media profile one" style="left:175px"></a>
  <a class="social" href="#" aria-label="Social media profile two" style="left:213px"></a>
  <a class="social" href="#" aria-label="Social media profile three" style="left:251px"></a>

  <div class="divider" style="left:330px"></div>
  <h4 class="foot-title" style="left:373px;top:3600px">QUICK LINKS</h4>
  <ul class="foot-list" style="left:373px;top:3634px">
    <li>Home</li><li>About Us</li><li>Why Choose Us</li><li>Services</li><li>Blog</li><li>Contact Us</li>
  </ul>

  <div class="divider" style="left:525px"></div>
  <h4 class="foot-title" style="left:567px;top:3600px">SERVICES</h4>
  <ul class="foot-list" style="left:567px;top:3634px">
    <li>Commercial Services</li><li>Light Commercial Services</li><li>Professional Laundry Services</li><li>Pickup and Delivery</li><li>Wash Dry Fold</li><li>Dry Cleaning</li>
  </ul>

  <div class="divider" style="left:773px"></div>
  <h4 class="foot-title" style="left:815px;top:3600px">CONTACT US</h4>
  <div class="contact-line" style="top:3630px">
    <svg width="10" height="14" viewBox="0 0 10 14" style="margin-top:5px"><path d="M5,0 C2.2,0 0,2.2 0,5 C0,8.5 5,14 5,14 C5,14 10,8.5 10,5 C10,2.2 7.8,0 5,0 Z" fill="#111"/><circle cx="5" cy="5" r="1.8" fill="#fff"/></svg>
    <span>12 Larkspur Row,<br>Atlanta</span>
  </div>
  <div class="contact-line" style="top:3690px">
    <svg width="11" height="9" viewBox="0 0 11 9" style="margin-top:8px"><rect width="11" height="9" fill="#111"/><path d="M0,0 L5.5,5 L11,0" fill="none" stroke="#fff" stroke-width="1"/></svg>
    <span>info@brightfoldlaundry.example</span>
  </div>
  <div class="contact-line" style="top:3723px">
    <svg width="11" height="11" viewBox="0 0 24 24" style="margin-top:7px"><path d="M6.6 10.8a15.1 15.1 0 0 0 6.6 6.6l2.2-2.2a1 1 0 0 1 1-.25 11.4 11.4 0 0 0 3.6.57 1 1 0 0 1 1 1V20a1 1 0 0 1-1 1A17 17 0 0 1 3 4a1 1 0 0 1 1-1h3.5a1 1 0 0 1 1 1c0 1.25.2 2.45.57 3.57a1 1 0 0 1-.25 1z" fill="#111"/></svg>
    <span>01 555 010 789</span>
  </div>

  <div class="abs" style="left:174px;top:3871px;width:795px;border-top:1px solid #cfcfcf"></div>
  <p class="abs" style="left:174px;top:3886px;font-size:11.5px;color:var(--ink);white-space:nowrap">© 2022 BRIGHTFOLD LAUNDRY COMPANY. All right reserved</p>
  <a class="abs" href="#" style="left:969px;top:3866px;width:59px;height:50px;background:#1b1b1b;color:#fff;font-family:var(--head);font-size:8px;letter-spacing:1px;text-align:center">
    <svg width="30" height="16" viewBox="0 0 30 16" style="margin-top:10px"><path d="M2,15 L15,2 L28,15" fill="none" stroke="#fff" stroke-width="1.3"/></svg>
    <span style="display:block;margin-top:2px">GO TO TOP</span>
  </a>
</footer>

</body>
</html>
```